Crafting Golden Harbors Conference Key Visual

Looking at a key visual design for a conference event

Target Market(s)

Corporates

Industry/Entity Type

Insurance Events

Font styles to use
Sans Serif

Colors
0054AA
0677BA
7BADD7
CADEEF
E8F1F8
EE7325
F08F49
F5BC92
FAE3D3
FDF4ED
EB3D1F
EC4F4E
F09395
F8D3D4
FCEDEE

Requirements
Must have
• An element of excitement
Should not have
• F1 Cars

```html
<!DOCTYPE html>
<html lang="en">
<head>
<meta charset="utf-8">
<title>Crafting Golden Harbors — Conference Key Visual</title>
<link rel="stylesheet" href="https://fonts.googleapis.com/css2?family=Staatliches&family=Roboto:wght@900&display=swap">
<style>
  :root {
    --page-bg: #ffffff;
    --sky-top: #2f6fb3;
    --sky-mid: #4d8fce;
    --horizon-glow: #cadeef;
    --trail-red: #eb3d1f;
    --trail-pink: #ec4f4e;
    --trail-amber: #f5bc3a;
    --trail-orange: #ee7325;
    --road-dark: #1c2530;
    --road-mid: #3c4a5a;
    --mark-red: #e02a2a;
    --title-fill: #ffffff;
    --title-stroke: #111111;
  }
  html, body {
    margin: 0;
    width: 1200px;
    height: 740px;
    overflow: hidden;
    background: var(--page-bg);
  }
  .canvas {
    position: relative;
    width: 1200px;
    height: 740px;
  }
  .key-visual {
    position: absolute;
    left: 76px;
    top: 75px;
    width: 1047px;
    height: 589px;
    overflow: hidden;
  }
  .scene-photo {
    position: absolute;
    inset: 0;
    background:
      radial-gradient(ellipse 30% 10% at 50% 60%, rgba(255,255,255,0.85), rgba(202,222,239,0) 70%),
      linear-gradient(165deg, rgba(0,0,0,0) 30%, rgba(245,188,58,0.45) 42%, rgba(236,79,78,0.45) 50%, rgba(0,0,0,0) 58%),
      linear-gradient(195deg, rgba(0,0,0,0) 30%, rgba(245,188,58,0.45) 42%, rgba(236,79,78,0.45) 50%, rgba(0,0,0,0) 58%),
      linear-gradient(180deg, var(--sky-top) 0%, var(--sky-mid) 45%, var(--trail-red) 58%, var(--road-mid) 64%, var(--road-dark) 100%);
  }
  .event-mark {
    position: absolute;
    left: 0;
    right: 0;
    top: 118px;
    height: 50px;
    display: flex;
    align-items: center;
    justify-content: center;
    gap: 12px;
  }
  .event-mark-dot {
    width: 30px;
    height: 30px;
    border-radius: 50%;
    background: var(--mark-red);
  }
  .event-mark-name {
    font-family: "Roboto", sans-serif;
    font-weight: 900;
    font-size: 44px;
    line-height: 1;
    color: var(--mark-red);
  }
  .event-title {
    position: absolute;
    left: 0;
    right: 0;
    top: 428px;
    margin: 0;
    text-align: center;
    font-family: "Staatliches", sans-serif;
    font-weight: 400;
    font-size: 88px;
    line-height: 1;
    letter-spacing: 2px;
    white-space: nowrap;
    color: var(--title-fill);
    -webkit-text-stroke: 2px var(--title-stroke);
    transform: skewX(-10deg);
  }
</style>
</head>
<body>
  <div class="canvas">
    <section class="key-visual">
      <div class="scene-photo" role="img" aria-label="Night city highway photo with symmetrical colourful light trails streaking towards skyscrapers on the horizon"></div>
      <div class="event-mark">
        <span class="event-mark-dot"></span>
        <span class="event-mark-name">Harbora</span>
      </div>
      <h1 class="event-title">Crafting Golden Harbors</h1>
    </section>
  </div>
</body>
</html>
```